Tree Pruning Website

We need a website for a tree Arborist, pruning company called Hollow Ridge Groundcare. We look after all types of trees, knock down trees and prune trees. Our target market is from domestic clients to government clients and everything in between.

We would like to see the use of our main colours which are orange and green

We are not looking forward in seeing a template that we have seen before but a unique template. We have designed 5 templates ourselves and we wish for the design community to take our designs to the next level.

We have also designed a template for things that **we are not** looking for (Version 4)

To make it fair for everyone, we are also not giving out any participation payments as we have had. One winner will take all of the payment!!!

I Have attached a image of the designs and a image of a tree.

We are just looking at the PSD file been developed. We have our own team who can slice the image up into a HTML format.

Target Market(s)

Everyone who needs to cut down a tree

Industry/Entity Type

Government

Requirements
Must have
• Logo on front page
A List of our services
jQuery slider on page
Phone Number on every page

```html
<!DOCTYPE html>
<html lang="en">
<head>
<meta charset="utf-8">
<title>Hollow Ridge Groundcare</title>
<link href="https://fonts.googleapis.com/css2?family=Cuprum:wght@400;700&family=Arimo&display=swap" rel="stylesheet">
<style>
:root{
  --header-dark:#2b7f2b;
  --header-light:#3f9a3a;
  --page-green:#45a445;
  --page-glow:#72c270;
  --footer-bg:#24452a;
  --footer-line:#3a6a40;
  --text-dark:#14301a;
  --text-white:#ffffff;
  --lime-top:#d6f56a;
  --lime-bottom:#9fd83a;
  --panel-grey:#d9d9d9;
  --orange-top:#f5b21c;
  --orange-bottom:#d9800a;
  --leaf:#8fd13d;
}
*{margin:0;padding:0;box-sizing:border-box}
html,body{width:1200px;height:1107px;overflow:hidden;background:var(--page-green)}
.site{position:absolute;left:0;top:0;width:1084px;height:1000px;transform:scale(1.107);transform-origin:0 0;
  background:radial-gradient(ellipse 600px 420px at 540px 560px,var(--page-glow),var(--page-green) 80%);font-family:"Arimo",Arial,sans-serif}
.site-header{position:absolute;left:0;top:0;width:1084px;height:115px;background:linear-gradient(var(--header-light),var(--header-dark));border-bottom:2px solid #5cb35a}
.brand{position:absolute;display:flex;align-items:center;gap:10px;font-family:"Cuprum",sans-serif;font-weight:700;color:var(--text-white);white-space:nowrap}
.brand-dot{flex:none;width:50px;height:50px;border-radius:50%;background:var(--leaf)}
.site-header .brand{left:20px;top:28px;font-size:26px;line-height:26px}
.main-nav{position:absolute;top:46px;left:0;font-family:"Cuprum",sans-serif;font-size:24px;color:var(--text-white);text-transform:uppercase}
.main-nav a{position:absolute;color:inherit;text-decoration:none;white-space:nowrap}
.main-nav a.active{border-bottom:2px solid #fff;line-height:27px}
.slider{position:absolute;left:44px;top:163px;width:686px;height:315px;background:linear-gradient(#f2f2f2,var(--panel-grey));border:1px solid #aaa;border-radius:4px;box-shadow:0 6px 16px rgba(0,0,0,.25)}
.slide-main{position:absolute;left:8px;top:9px;width:557px;height:270px;background:linear-gradient(160deg,#a8c84a,#4f6e1e 45%,#2e3f12);border:1px solid #555}
.slide-thumb{position:absolute;left:568px;width:104px;border:1px solid #888}
.slider-dots{position:absolute;left:304px;top:285px;display:flex;gap:11px}
.slider-dots span{width:19px;height:19px;border-radius:50%;background:#fafafa;border:1px solid #999}
.slider-dots span.on{background:radial-gradient(circle at 40% 35%,#9fe05a,#3a9a1c);border-color:#2a7a10}
.gallery-label{position:absolute;right:20px;top:287px;font-family:"Cuprum",sans-serif;font-weight:700;font-size:16px;color:#444}
.side-box{position:absolute;left:748px;top:163px;width:325px;height:312px;background:rgba(40,110,40,.35);border:1px solid rgba(255,255,255,.2);border-radius:4px}
.side-title{height:40px;background:linear-gradient(var(--lime-top),var(--lime-bottom));border-radius:4px 4px 0 0;text-align:center;font-family:"Cuprum",sans-serif;font-weight:700;font-size:18px;line-height:42px;color:#245a1a}
.side-body{position:absolute;left:10px;top:51px;width:305px;height:248px;background:rgba(20,70,20,.4);border-radius:3px;padding:6px 10px 6px 6px;font-size:14px;line-height:19.3px;color:#f2f7ee}
.btn-more{position:absolute;right:8px;bottom:8px;width:92px;height:33px;background:linear-gradient(var(--orange-top),var(--orange-bottom));border:1px solid #a85e00;border-radius:4px;font-family:"Cuprum",sans-serif;font-weight:700;font-size:16px;line-height:31px;text-align:center;color:#3a2000}
.intro{position:absolute;left:50px;top:514px;width:998px;height:322px;background:rgba(120,200,120,.25);padding:4px 8px;overflow:hidden}
.intro-lead{font-family:"Cuprum",sans-serif;font-size:24.5px;line-height:31px;color:var(--text-dark);margin-bottom:22px}
.intro-lead b{font-weight:700}
.intro p.body{font-size:14.4px;line-height:17.6px;color:#1a2a18;width:935px;margin-left:2px;margin-bottom:4px}
.site-footer{position:absolute;left:0;top:866px;width:1084px;height:134px;background:var(--footer-bg);border-top:2px solid var(--footer-line)}
.footer-info{position:absolute;left:60px;top:20px;font-family:"Cuprum",sans-serif;font-weight:700;font-size:17px;line-height:23px;color:#0f1f10;text-transform:uppercase}
.footer-divider{position:absolute;left:522px;top:8px;width:2px;height:114px;background:#142a16}
.site-footer .brand{left:540px;top:36px;font-size:24px;line-height:25px}
.footer-note{position:absolute;left:774px;top:11px;width:302px;font-size:13.5px;line-height:19px;color:#cfe0cc}
</style>
</head>
<body>
<div class="site">
  <header class="site-header">
    <div class="brand"><span class="brand-dot"></span><span>Hollow Ridge<br>Groundcare</span></div>
    <nav class="main-nav">
      <a class="active" style="left:368px" href="#">Home</a>
      <a style="left:479px" href="#">About Us</a>
      <a style="left:619px" href="#">Our Services</a>
      <a style="left:789px" href="#">Get a Quote</a>
      <a style="left:949px" href="#">Contact Us</a>
    </nav>
  </header>

  <section class="slider">
    <div class="slide-main" role="img" aria-label="Photo of a sunlit woodland path lined with tall trees"></div>
    <div class="slide-thumb" style="top:13px;height:89px;background:linear-gradient(#e8e29a,#5a8a2a 60%,#2e5a18)" role="img" aria-label="Photo of sun shining through a forest"></div>
    <div class="slide-thumb" style="top:106px;height:89px;background:linear-gradient(#2a6ad0,#3f7a2a 55%,#4ea22a)" role="img" aria-label="Photo of a large tree under a blue sky"></div>
    <div class="slide-thumb" style="top:199px;height:78px;background:linear-gradient(#5a8ad8,#6a7a5a 55%,#4a8a2a)" role="img" aria-label="Photo of bare trees in a park"></div>
    <div class="slider-dots"><span class="on"></span><span></span><span></span><span></span></div>
    <div class="gallery-label">Photo Gallery</div>
  </section>

  <aside class="side-box">
    <div class="side-title">Lorem Ipsum</div>
    <div class="side-body">Lorem ipsum dolor sit amet, consectetur adipiscing elit. Morbi ut nisl purus, eget tristique turpis. Vestibulum ut tellus nisi. Donec sit amet lectus id turpis pulvinar sollicitudin et ac sapien. Vivamus nisi lorem, ornare sit amet iaculis quis, aliquet id sapien. Fusce quis libero ultrices tortor auctor consequat eu vitae est. Proin ac mattis augue. Integer lobortis porttitor augue non pellentesque.
      <div class="btn-more">Read More</div>
    </div>
  </aside>

  <section class="intro">
    <p class="intro-lead">Lorem Ipsum dolor sit amet, consectetur adipiscing elit. <b>Morbi ut</b> nisl purus, eget tristique turpis. Ut tell us nisi. Donec sit amet lectus id turpis <b>pulvinar</b> sollicitudin et ac saplen. Vivamus nisi lorem, orn sit amet <b>iacullis quis</b>, aliquet id saplen.</p>
    <p class="body">Proin eget lorem sit amet ligula luctus pulvinar. Sed elementum neque ac ligula aliquam ultrices. Maecenas vitae nunc id metus pellentesque pellentesque eleifend sed erat. Integer dignissim accumsan ligula, vitae pharetra leo bibendum a. Integer mollis accumsan volutpat. Cras acl lobortis metus. Mauris et enim at leo venenatis sodales. Suspendisse vitae ipsum vel nisi tincidunt imperdiet. Integer non elit nunc, vel moles tie diam. Etiam egestas imperdiet odio, ac aliquet metus facilisis a. Cras molestie sagittis felis vel placerat. Mauris varius odio in massa iaculis quis bibendum quam pretium. Proin faucibus nisl eu ligula porta id pharetra magna porta. Nullam et turpis id erat sagittis pulvinar eu quis quam. Nunc porttitor leo hendrerit metus mollis lacinia.</p>
    <p class="body">ras gravida fringilla feugiat. Ut sed rhoncus ipsum. Quisque non nibh lectus, nec sodales velit. Cras velit diam, dapibus interdum cursus sed, venenatis sit amet dolor. Aenean auctor purus non nibh adipiscing vitae ultrices est bibendum. Lorem ipsum dolor sit amet, consectetur adipiscing elit. Class aptent taciti sociosqu ad litora torquent per conubia nostra, per inceptos himenaeos. Aenean felis odio, vehicula ac cursus vel, rhoncus non mi. Nulla facilisi.</p>
  </section>

  <footer class="site-footer">
    <div class="footer-info">
      Hollow Ridge Groundcare (c) I All rights reserved I 2013<br>
      Contact us: 08 5550 1420<br>
      Fax: 08 5550 1421<br>
      17 Marlow Lane, Fernbrook, WA 6999
    </div>
    <div class="footer-divider"></div>
    <div class="brand"><span class="brand-dot"></span><span>Hollow Ridge<br>Groundcare</span></div>
    <p class="footer-note">Sed tortor quam, vehicula ac dictum eu, aliquam ut mauris. Vestibulum tempus, urna et elementum convallis, justo lorem consectetur sem, sit amet accumsan lorem sapien eget velit. Phasellus adipiscing elit id felis eleifend eu vestibulum sapien cursus.</p>
  </footer>
</div>
</body>
</html>
```